TriVex Business Card Design - double sided -plumbing local plumbing company

We have a Plumbing company where the design was create through Sketch Hive. We would now like a business card designed as well. We want it to be in the colour version of the logo.

Details below for the card.

Phone Number: 0438 615 247
Email: info@trivexplumbing.example.au
Website: https://trivexplumbing.example.au
We really want a sophisticated design that stand out from the other- informative and timeless.

Target Market(s)

local Canberra market

Industry/Entity Type

Plumbing, gas fitting, hot water

Contact Information for Business Card

Phone number, email, logo and "Supplying all your heating, cooling and hot water needs"

Requirements
Must have
• bust be colourful, must also be though about it being printed on a magnet. must Vex with the logo - I dont want the logo and information chucked onto a white canvas I would prefer it to be smooth and look purposeful

```html
<!DOCTYPE html>
<html lang="en">
<head>
<meta charset="UTF-8">
<title>TriVex Plumbing – Business Card</title>
<link href="https://fonts.googleapis.com/css2?family=Roboto:wght@400;500;700&display=swap" rel="stylesheet">
<style>
  :root {
    --stage: #2b2b2d;
    --card: #1e1e20;
    --card-edge: #262628;
    --ink: #f2f2f2;
    --ink-muted: #bdbdbd;
    --brand-blue: #2f7fd0;
    --brand-orange: #f0a321;
    --mark-tone: #2c2c2f;
    --mark-light: #48484c;
  }
  * { box-sizing: border-box; margin: 0; padding: 0; }
  html, body {
    width: 1200px; height: 852px; overflow: hidden;
    background: var(--stage);
    font-family: "Roboto", Arial, sans-serif;
  }
  .canvas {
    width: 1200px; height: 852px;
    display: flex; align-items: center; justify-content: center; gap: 50px;
  }
  .card {
    position: relative;
    width: 540px; height: 330px;
    border-radius: 22px;
    background: linear-gradient(145deg, var(--card-edge), var(--card));
    box-shadow: 0 18px 40px rgba(0,0,0,.45);
    overflow: hidden;
    color: var(--ink);
  }

  /* Front */
  .card--front .brand {
    position: absolute; left: 0; right: 0; top: 118px;
    display: flex; align-items: center; justify-content: center; gap: 14px;
  }
  .brand__dot {
    width: 26px; height: 26px; border-radius: 50%;
    background: var(--mark-light);
  }
  .brand__name {
    font-weight: 700; font-size: 50px; letter-spacing: 1px;
    color: var(--mark-light);
  }
  .card--front .tagline {
    position: absolute; left: 0; right: 0; top: 200px;
    text-align: center; font-size: 15px; color: var(--ink);
  }
  .hl-orange { color: var(--brand-orange); }
  .hl-blue { color: var(--brand-blue); }

  /* Back */
  .card--back .mark {
    position: absolute; left: -40px; top: 70px;
    width: 300px; height: 300px; border-radius: 50%;
    background: radial-gradient(circle at 60% 35%, var(--mark-light), var(--mark-tone) 65%);
  }
  .details {
    position: absolute; right: 34px; top: 30px;
    text-align: right;
  }
  .details__name { font-size: 20px; font-weight: 700; color: var(--brand-blue); }
  .details__role { font-size: 13px; color: var(--ink); margin-top: 2px; }
  .details__tagline {
    margin-top: 18px; padding-right: 12px;
    border-right: 3px solid var(--brand-orange);
    font-size: 13.5px; line-height: 1.3; color: var(--brand-blue);
  }
  .contact { list-style: none; margin-top: 18px; font-size: 13.5px; line-height: 1.55; color: var(--ink); }
  .contact li { display: flex; justify-content: flex-end; align-items: center; gap: 7px; }
  .contact svg { width: 12px; height: 12px; fill: var(--brand-blue); flex: none; }
  .contact li.no-icon { padding-right: 19px; }
</style>
</head>
<body>
<main class="canvas">
  <section class="card card--front" aria-label="Business card front">
    <div class="brand">
      <span class="brand__dot"></span>
      <span class="brand__name">TriVex Plumbing</span>
    </div>
    <p class="tagline">Supplying all your <span class="hl-orange">heating</span>, <span class="hl-blue">cooling</span> and <span class="hl-orange">hot water</span> needs</p>
  </section>

  <section class="card card--back" aria-label="Business card back">
    <div class="mark" aria-hidden="true"></div>
    <div class="details">
      <h1 class="details__name">Marcus Hale</h1>
      <p class="details__role">Managing Director</p>
      <p class="details__tagline">Supplying all your<br>heating, cooling and<br>hot water needs</p>
      <ul class="contact">
        <li>0438 615 247
          <svg viewBox="0 0 24 24" aria-hidden="true"><path d="M6.6 10.8a15 15 0 0 0 6.6 6.6l2.2-2.2c.3-.3.7-.4 1-.2 1.1.4 2.3.6 3.6.6.6 0 1 .4 1 1V20c0 .6-.4 1-1 1A17 17 0 0 1 3 4c0-.6.4-1 1-1h3.5c.6 0 1 .4 1 1 0 1.3.2 2.5.6 3.6.1.3 0 .7-.2 1z"/></svg>
        </li>
        <li>info@trivexplumbing.example.au
          <svg viewBox="0 0 24 24" aria-hidden="true"><path d="M2 5h20v14H2z M4 7v.5l8 5 8-5V7l-8 5z"/></svg>
        </li>
        <li>https://trivexplumbing.example.au
          <svg viewBox="0 0 24 24" aria-hidden="true"><path d="M12 2a10 10 0 1 0 0 20 10 10 0 0 0 0-20zm6.9 6h-3a15 15 0 0 0-1.3-3.6A8 8 0 0 1 18.9 8zM12 4c.8 1.2 1.5 2.5 1.9 4h-3.8c.4-1.5 1.1-2.8 1.9-4zM4.3 14a8 8 0 0 1 0-4h3.4a16 16 0 0 0 0 4zm.8 2h3a15 15 0 0 0 1.3 3.6A8 8 0 0 1 5.1 16zm3-8h-3a8 8 0 0 1 4.3-3.6C8.8 5.6 8.4 6.8 8.1 8zM12 20c-.8-1.2-1.5-2.5-1.9-4h3.8c-.4 1.5-1.1 2.8-1.9 4zm2.3-6H9.7a14 14 0 0 1 0-4h4.6a14 14 0 0 1 0 4zm.3 5.6c.6-1.1 1-2.3 1.3-3.6h3a8 8 0 0 1-4.3 3.6zm1.7-5.6a16 16 0 0 0 0-4h3.4a8 8 0 0 1 0 4z"/></svg>
        </li>
      </ul>
    </div>
  </section>
</main>
</body>
</html>
```